Vornel Technologies business card design

We need a business card designed with our new logo. it would be great if the card could communicate it is a technology based company.

Target Market(s)

system integrators

Industry/Entity Type

technology, IOT

Contact Information for Business Card

Name, designation, Address, telephone number, email address

Requirements
Must have
• logo and company name
Nice to have
• something to do with technology

```html
<!DOCTYPE html>
<html lang="en">
<head>
<meta charset="utf-8">
<title>Vornel Technologies – Business Card</title>
<link href="https://fonts.googleapis.com/css2?family=Roboto:wght@400;500;700&display=swap" rel="stylesheet">
<style>
  :root {
    --page-bg: #f1f1f1;
    --card-bg: #ffffff;
    --ink: #3a3b3d;
    --accent: #f7931e;
    --card-edge: #e2e2e2;
  }
  * { box-sizing: border-box; margin: 0; padding: 0; }
  html, body {
    width: 1200px; height: 896px; overflow: hidden;
    background: var(--page-bg);
    font-family: "Roboto", Arial, sans-serif;
    color: var(--ink);
  }
  .card {
    position: absolute;
    left: 335px;
    width: 529px;
    height: 303px;
    background: var(--card-bg);
    border: 1px solid var(--card-edge);
    border-radius: 26px;
  }
  .card--front { top: 125px; }
  .card--back  { top: 473px; }

  .brand {
    position: absolute;
    display: flex;
    align-items: center;
    gap: 10px;
    font-weight: 700;
    color: var(--ink);
    white-space: nowrap;
  }
  .brand__square { background: var(--accent); flex: none; }
  .card--front .brand { left: 20px; top: 36px; font-size: 30px; }
  .card--front .brand__square { width: 22px; height: 22px; }
  .card--back .brand {
    left: 0; right: 0; top: 122px; justify-content: center;
    font-size: 46px; gap: 16px;
  }
  .card--back .brand__square { width: 34px; height: 34px; }

  .person { position: absolute; left: 21px; top: 152px; }
  .person__name { font-size: 20px; font-weight: 500; color: var(--accent); line-height: 1.1; }
  .person__role { font-size: 12.5px; margin-top: 6px; }

  .divider {
    position: absolute; left: 20px; right: 18px; top: 209px;
    height: 1.5px; background: var(--accent);
  }

  .contacts { position: absolute; left: 20px; top: 222px; list-style: none; }
  .contacts li {
    display: flex; align-items: center; gap: 4px;
    font-size: 12px; height: 20px;
  }
  .contacts svg { width: 11px; height: 11px; fill: var(--accent); flex: none; }

  .address {
    position: absolute; right: 22px; top: 243px;
    font-size: 12px; text-align: right; line-height: 20px; font-style: normal;
  }
</style>
</head>
<body>

<section class="card card--front" aria-label="Card front">
  <div class="brand"><span class="brand__square"></span>Vornel Technologies</div>

  <div class="person">
    <p class="person__name">DARIN KOLVEK</p>
    <p class="person__role">Managing Director</p>
  </div>

  <div class="divider"></div>

  <ul class="contacts">
    <li>
      <svg viewBox="0 0 24 24" aria-hidden="true"><path d="M6.6 10.8a15.1 15.1 0 0 0 6.6 6.6l2.2-2.2a1 1 0 0 1 1-.25 11.4 11.4 0 0 0 3.6.57 1 1 0 0 1 1 1V20a1 1 0 0 1-1 1A17 17 0 0 1 3 4a1 1 0 0 1 1-1h3.5a1 1 0 0 1 1 1c0 1.25.2 2.45.57 3.57a1 1 0 0 1-.25 1z"/></svg>
      555 218 407
    </li>
    <li>
      <svg viewBox="0 0 24 24" aria-hidden="true"><path d="M2 5h20v2l-10 6L2 7z M2 9l10 6 10-6v10H2z"/></svg>
      info@vornelmail.com
    </li>
    <li>
      <svg viewBox="0 0 24 24" aria-hidden="true"><path d="M12 2a10 10 0 1 0 0 20 10 10 0 0 0 0-20zm-1 17.9A8 8 0 0 1 4.2 10L9 14.8v1a2 2 0 0 0 2 2zm6.9-2.5A2 2 0 0 0 16 16h-1v-3a1 1 0 0 0-1-1H8v-2h2a1 1 0 0 0 1-1V7h2a2 2 0 0 0 2-2v-.4a8 8 0 0 1 2.9 12.8z"/></svg>
      www.vornelsite.com
    </li>
  </ul>

  <address class="address">
    1870 Harbor Crest Lane<br>
    Bayview CA 90417
  </address>
</section>

<section class="card card--back" aria-label="Card back">
  <div class="brand"><span class="brand__square"></span>Vornel Technologies</div>
</section>

</body>
</html>
```